Meridale Legal Letterhead for Law firm must be modern and use the logo I uploaded.

Hello I want a clean modern professional letterhead for my law firm Meridale Legal. A logo has already been created and all files have been uploaded. The information for the firm can be given through message. Please use the logo that has already been created. Please also use the color scheme of that logo. (blue and white).

Target Market(s)

General Public

Industry/Entity Type

Law Firm

Colors

Designer to choose colors to be used in the design.

Requirements
Must have
• This must be a modern professional letterhead
Nice to have
• My logo that is included in file form
Should not have
• Should not have logo that is not the one I uploaded.

```html
<!DOCTYPE html>
<html lang="en">
<head>
<meta charset="utf-8">
<title>Meridale Legal Letterhead</title>
<link href="https://fonts.googleapis.com/css2?family=Roboto:wght@400;500;700&display=swap" rel="stylesheet">
<style>
  :root {
    --navy: #2d3263;
    --backdrop: #e6e6e6;
    --paper: #ffffff;
    --footer-grey: #838383;
    --frame-line: #d4d4dc;
    --meta-text: #5e5e5e;
    --body-text: #333333;
    --faint-tone: #f6f6f6;
  }
  * { margin: 0; padding: 0; box-sizing: border-box; }
  html, body {
    width: 1150px;
    height: 1200px;
    overflow: hidden;
    background: var(--backdrop);
    font-family: "Roboto", sans-serif;
  }
  .letterhead {
    position: absolute;
    left: 190px;
    top: 102px;
    width: 770px;
    height: 995px;
    background: var(--paper);
    overflow: hidden;
  }
  .corner-accent { position: absolute; }
  .corner-accent--top { left: 0; top: 0; }
  .corner-accent--bottom { right: 0; bottom: 0; z-index: 2; }

  .background-panel {
    position: absolute;
    left: 220px;
    top: 212px;
    width: 480px;
    height: 480px;
    background: var(--faint-tone);
  }

  .content-frame {
    position: absolute;
    left: 69px;
    top: 77px;
    width: 631px;
    height: 841px;
    border: 1px solid var(--frame-line);
  }
  .masthead {
    position: absolute;
    left: 251px;
    top: 30px;
    width: 268px;
    height: 148px;
    background: var(--paper);
    text-align: center;
  }
  .masthead__mark {
    display: block;
    width: 34px;
    height: 34px;
    margin: 42px auto 0;
    background: var(--navy);
  }
  .masthead__name {
    margin-top: 34px;
    font-size: 21px;
    font-weight: 500;
    letter-spacing: 8px;
    color: var(--navy);
    text-transform: uppercase;
    padding-left: 8px;
    white-space: nowrap;
  }

  .letter-meta {
    position: absolute;
    right: 118px;
    top: 224px;
    text-align: right;
    color: var(--meta-text);
    font-size: 14px;
    line-height: 20px;
  }
  .letter-meta__date { margin-bottom: 10px; }
  .letter-meta__recipient { font-weight: 700; }

  .letter-body {
    position: absolute;
    left: 136px;
    top: 380px;
    width: 516px;
    color: var(--body-text);
    font-size: 13.5px;
    letter-spacing: -0.15px;
    line-height: 25px;
    text-align: justify;
  }
  .letter-body p + p { margin-top: 24.5px; }

  .contact-bar {
    position: absolute;
    left: 0;
    top: 951px;
    width: 770px;
    height: 44px;
    background: var(--footer-grey);
    color: #ffffff;
    font-size: 11px;
    text-transform: uppercase;
  }
  .contact-item {
    position: absolute;
    top: 0;
    height: 44px;
    display: flex;
    align-items: center;
    gap: 8px;
    white-space: nowrap;
  }
  .contact-item--address { left: 62px; }
  .contact-item--phone { left: 385px; }
  .contact-item--web { left: 522px; }
  .contact-item svg { width: 15px; height: 15px; flex: none; }
</style>
</head>
<body>
  <main class="letterhead">
    <svg class="corner-accent corner-accent--top" width="74" height="167" viewBox="0 0 74 167" aria-hidden="true">
      <polygon points="0,0 73,0 0,166" fill="var(--navy)"/>
    </svg>

    <div class="background-panel" role="img" aria-label="Faint background decoration in the brand tone"></div>

    <div class="content-frame"></div>

    <header class="masthead">
      <span class="masthead__mark" aria-hidden="true"></span>
      <div class="masthead__name">Meridale Legal</div>
    </header>

    <section class="letter-meta">
      <div class="letter-meta__date">November 16, 2023</div>
      <div class="letter-meta__recipient">Recippient Name</div>
      <div>Vice President</div>
      <div>Example Incooration</div>
      <div>State</div>
    </section>

    <article class="letter-body">
      <p>Lorem ipsum dolor sit amet, consectetur adipiscing elit. Phasellus nec velit sed ligula facilisis malesuada interdum non urna. Aliquam auctor eros sed gravida viverra. Mauris fringilla ac elit vitae laoreet. Integer condimentum vel lectus non eleifend. Quisque facilisis faucibus blandit. Proin vestibulum dapibus ipsum eu commodo. Nullam hendrerit lectus nec lectus venenatis mattis.</p>
      <p>Vestibulum ornare lorem sed feugiat faucibus. Morbi efficitur sapien ut tellus pellentesque, a lacinia nisi fermentum. Sed viverra mi lacus, ac scelerisque nisl fringilla at. Nullam lectus ipsum, laoreet ac libero eget, dapibus faucibus magna. Orci varius natoque penatibus et magnis dis parturient montes, nascetur ridiculus mus. Integer in posuere orci. Pellentesque euismod ut ante eu elementum. Ut consectetur ac urna sed varius. Aliquam consectetur tortor erat, non aliquet libero accumsan id.</p>
      <p>Nunc magna purus, fermentum ut nulla vitae, aliquet placerat urna. Donec leo justo, ornare quis lectus sit amet, aliquam venenatis diam. Vivamus pharetra dui ut quam sagittis dignissim. Aliquam eget turpis purus. Aliquam erat volutpat. Etiam sed ultricies purus, bibendum porttitor neque.</p>
    </article>

    <footer class="contact-bar">
      <div class="contact-item contact-item--address">
        <svg viewBox="0 0 16 16" aria-hidden="true">
          <circle cx="8" cy="8" r="7.5" fill="#ffffff"/>
          <path d="M8 3.2a3 3 0 0 0-3 3c0 2.2 3 6 3 6s3-3.8 3-6a3 3 0 0 0-3-3z" fill="var(--footer-grey)"/>
          <circle cx="8" cy="6.2" r="1.1" fill="#ffffff"/>
        </svg>
        <span>Name of Street, City, Province, Country</span>
      </div>
      <div class="contact-item contact-item--phone">
        <svg viewBox="0 0 16 16" aria-hidden="true">
          <circle cx="8" cy="8" r="7.5" fill="#ffffff"/>
          <path d="M5.3 4.2l1.3-.3.9 2-.9.8c.5 1 1.2 1.7 2.2 2.2l.8-.9 2 .9-.3 1.3c-.2.5-.7.7-1.2.6C7.5 10.2 5.8 8.5 5.1 5.9c-.1-.6.1-1.3.2-1.7z" fill="var(--footer-grey)"/>
        </svg>
        <span>00 123 456 789</span>
      </div>
      <div class="contact-item contact-item--web">
        <svg viewBox="0 0 16 16" aria-hidden="true">
          <circle cx="8" cy="8" r="6.8" fill="none" stroke="#ffffff" stroke-width="1.2"/>
          <ellipse cx="8" cy="8" rx="3" ry="6.8" fill="none" stroke="#ffffff" stroke-width="1"/>
          <line x1="1.2" y1="8" x2="14.8" y2="8" stroke="#ffffff" stroke-width="1"/>
          <line x1="2.4" y1="4.6" x2="13.6" y2="4.6" stroke="#ffffff" stroke-width="0.9"/>
          <line x1="2.4" y1="11.4" x2="13.6" y2="11.4" stroke="#ffffff" stroke-width="0.9"/>
        </svg>
        <span>www.meridalelegal.com</span>
      </div>
    </footer>

    <svg class="corner-accent corner-accent--bottom" width="64" height="144" viewBox="0 0 64 144" aria-hidden="true">
      <polygon points="64,0 64,144 0,144" fill="var(--navy)"/>
    </svg>
  </main>
</body>
</html>
```